Non-Fiction Book Cover Series Concepts

I need front cover concepts for a non-fiction business book series. Just concepts at this stage to show to backers (full cover designs later).

The books are for leaders and business owners. A mature, sophisticated market, AND, bold and innovative.

The series needs to be extensible - the concepts need to be able to work across at least 40 books. I am happy with a colour theme, or contrasts, or icon theme, there is no limitation to the imagination.

The books need to look like they belong to a series and to also stand alone.

I prefer simple and bold.

Imagine the Heron trade series (https://www.heronbooks.example/series/tws/heron-trade-wisdom-series.html) - but I hate these designs (the colours don't work for me).

The imprint is MindfulVantagePress.example - the logo mark for the imprint is attached.

The books will be printed and ebooks - the printed version will be 5 inches by 8 inches form factor. They will be printed with a matt cover.

IF YOU WANT A BOOK TITLE TO TRY, use this:

Steady Momentum: Apply the R.A.V. Model to Inspire, Unlock and Sustain Talent

Thank you for your interest!

Target Market(s)

Business owners, leaders, entrepreneurs

Industry/Entity Type

Leadership

Font styles to use
Serif
Sans Serif

Requirements
Must have
• Extensible - the concept can work for many books and ALL books look part of the series
Nice to have
• I prefer simple, icons rather than photos
Should not have
• No photographic designs - icon, drawing

```html
<!DOCTYPE html>
<html lang="en">
<head>
<meta charset="utf-8">
<title>Series Cover Concepts</title>
<link rel="stylesheet" href="https://fonts.googleapis.com/css2?family=Montserrat:wght@700;900&family=Jost:wght@400&display=swap">
<style>
  :root {
    --page: #ffffff;
    --paper: #f7f6f4;
    --ink: #1c1a2a;
    --grey-field: #cacaca;
    --grey-badge: #777777;
    --plum-field: #dcc4d8;
    --plum-badge: #995b8d;
    --sky-field: #b7e4ef;
    --sky-badge: #1ad8fa;
    --title: #ffffff;
  }
  * { margin: 0; padding: 0; box-sizing: border-box; }
  html, body { width: 1200px; height: 1200px; overflow: hidden; background: var(--page); }
  .sheet { position: relative; width: 1200px; height: 1200px; }

  .cover {
    position: absolute;
    width: 317px;
    height: 490px;
    background: var(--paper);
    box-shadow: 3px 4px 7px rgba(0, 0, 0, 0.22);
  }
  .cover--tall { height: 508px; }
  .cover--grey { left: 156px; top: 114px; --field: var(--grey-field); --badge: var(--grey-badge); }
  .cover--plum { left: 638px; top: 114px; --field: var(--plum-field); --badge: var(--plum-badge); }
  .cover--sky  { left: 441px; top: 666px; --field: var(--sky-field);  --badge: var(--sky-badge); }

  .field {
    position: absolute;
    left: 16px; top: 16px;
    width: 285px; height: 361px;
    background: var(--field);
  }
  .cover--tall .field { height: 375px; }

  .title { position: absolute; left: 0; top: 0; width: 285px; height: 300px; overflow: visible; }
  .cover--tall .title { top: 6px; }
  .title text {
    font-family: "Montserrat", sans-serif;
    font-weight: 900;
    fill: var(--title);
  }

  .author {
    position: absolute;
    left: 105px; top: 327px;
    width: 106px; height: 106px;
    border-radius: 50%;
    background: var(--badge);
    color: #ffffff;
    font-family: "Jost", sans-serif;
    font-weight: 400;
    font-size: 16px;
    line-height: 16px;
    text-align: center;
    display: flex;
    align-items: center;
    justify-content: center;
  }
  .cover--tall .author { top: 341px; }

  .imprint {
    position: absolute;
    left: 0; right: 0; top: 456px;
    text-align: center;
    font-family: "Montserrat", sans-serif;
    font-weight: 700;
    font-size: 9px;
    letter-spacing: 1px;
    color: var(--ink);
  }
  .cover--tall .imprint { top: 473px; }
</style>
</head>
<body>
<main class="sheet">

  <article class="cover cover--grey">
    <div class="field">
      <svg class="title" viewBox="0 0 285 300" aria-label="Title of this book">
        <text x="9" y="90" font-size="84" textLength="253" lengthAdjust="spacingAndGlyphs">TITLE</text>
        <text x="95" y="140" font-size="60" textLength="86" lengthAdjust="spacingAndGlyphs">OF</text>
        <text x="25" y="211" font-size="84" textLength="224" lengthAdjust="spacingAndGlyphs">THIS</text>
        <text x="0" y="283" font-size="90" textLength="285" lengthAdjust="spacingAndGlyphs">BOOK</text>
      </svg>
    </div>
    <div class="author">AUTHOR<br>NAME</div>
    <div class="imprint">BRIGHTWATER</div>
  </article>

  <article class="cover cover--tall cover--plum">
    <div class="field">
      <svg class="title" viewBox="0 0 285 300" aria-label="Title of this book">
        <text x="9" y="90" font-size="84" textLength="253" lengthAdjust="spacingAndGlyphs">TITLE</text>
        <text x="95" y="140" font-size="60" textLength="86" lengthAdjust="spacingAndGlyphs">OF</text>
        <text x="25" y="211" font-size="84" textLength="224" lengthAdjust="spacingAndGlyphs">THIS</text>
        <text x="0" y="283" font-size="90" textLength="285" lengthAdjust="spacingAndGlyphs">BOOK</text>
      </svg>
    </div>
    <div class="author">AUTHOR<br>NAME</div>
    <div class="imprint">BRIGHTWATER</div>
  </article>

  <article class="cover cover--tall cover--sky">
    <div class="field">
      <svg class="title" viewBox="0 0 285 300" aria-label="Title of this book">
        <text x="9" y="90" font-size="84" textLength="253" lengthAdjust="spacingAndGlyphs">TITLE</text>
        <text x="95" y="140" font-size="60" textLength="86" lengthAdjust="spacingAndGlyphs">OF</text>
        <text x="25" y="211" font-size="84" textLength="224" lengthAdjust="spacingAndGlyphs">THIS</text>
        <text x="0" y="283" font-size="90" textLength="285" lengthAdjust="spacingAndGlyphs">BOOK</text>
      </svg>
    </div>
    <div class="author">AUTHOR<br>NAME</div>
    <div class="imprint">BRIGHTWATER</div>
  </article>

</main>
</body>
</html>
```